Social Media Marketing website

Need website designed for social media marketing company BrightLoop.com
Do no currently have logo.
Pages:
Main
Services
Order
Contact
Please use dummy text for now. I will provide content to winner later to add.
Main page should clearly show the steps with some sort of graphic: Establish, Engage, Analyze.
Services provided (steps):
1) Establish social media presence
2) Social media management and advertising
3) Analyze and engage
Site should be simple, clean and attractive. Design examples:
http://plinkster.com/
http://www.quillbase.com/
http://www.harrowvalemq.com/
Be creative! It should not look like a template.
Updates
Updated examples.
Contact me for questions.
dave@brightloop.com
3) Analyze and engage
Advertising

```html
<!DOCTYPE html>
<html lang="en">
<head>
<meta charset="utf-8">
<title>BrightLoop – Social media marketing</title>
<link rel="stylesheet" href="https://fonts.googleapis.com/css2?family=Arimo:ital,wght@0,400;0,700;1,400;1,700&family=Open+Sans:ital,wght@0,400;0,600;0,700;1,700&family=Gochi+Hand&display=swap">
<style>
:root{
  --green:#3f9a0c;
  --green-dark:#2d7a05;
  --green-bright:#5cb814;
  --green-light:#7fcc2a;
  --page-bg:#ececec;
  --panel:#ffffff;
  --soft:#f2f2f2;
  --text:#222;
  --muted:#9a9a9a;
  --heading:#555;
}
*{margin:0;padding:0;box-sizing:border-box}
html,body{width:1200px;height:1109px;overflow:hidden}
body{
  position:relative;
  background:linear-gradient(#ffffff 0,#e6f0dc 132px,var(--green) 132px,var(--green) 134px,var(--page-bg) 134px);
  font-family:"Arimo",Arial,sans-serif;color:var(--text);
}
.page{position:absolute;left:178px;top:0;width:844px;height:1038px;background:var(--panel);box-shadow:0 0 14px rgba(0,0,0,.18)}
.abs{position:absolute;white-space:nowrap}

/* header */
.site-header{left:0;top:0;width:844px;height:89px;background:linear-gradient(#fff,#f3f3f3)}
.brand{left:37px;top:28px}
.brand-name{font-family:"Open Sans",sans-serif;font-weight:700;font-size:28px;color:var(--green-bright);line-height:1}
.brand-tag{font-family:"Open Sans",sans-serif;font-weight:600;font-style:italic;font-size:9.5px;color:var(--green);margin:3px 0 0 46px}
.social{top:46px;display:flex;align-items:center;gap:8px;font-family:"Gochi Hand",cursive;font-size:13.5px;color:var(--green-bright)}
.social .sq{width:21px;height:21px;border-radius:3px}
.social-follow{left:529px}
.social-fan{left:708px}

/* nav */
.main-nav{left:0;top:89px;width:844px;height:44px;background:linear-gradient(var(--green-light),var(--green) 60%,#3c9609);display:flex;align-items:center;padding-left:27px}
.main-nav a{color:#fff;text-decoration:none;font-size:14px;padding:0 8px;line-height:26px;border-left:1px solid rgba(255,255,255,.3)}
.main-nav a:first-child{border-left:0}

/* hero */
.hero{left:0;top:133px;width:844px;height:268px;background:radial-gradient(ellipse at 30% 30%,#6cc41d,#44a00c 60%,#388c08);overflow:hidden}
.hero-title{left:40px;top:26px;font-family:"Open Sans",sans-serif;font-style:italic;font-weight:700;font-size:28px;color:#fff;text-shadow:0 1px 2px rgba(0,0,0,.3)}
.hero-text{left:40px;top:80px;width:330px;white-space:normal;font-family:"Open Sans",sans-serif;font-size:12px;line-height:18.7px;color:#f2fbe8}
.btn-try{left:224px;top:191px;width:105px;height:38px;border-radius:3px;background:linear-gradient(#fff,#dcdcdc);border:2px solid #eee;box-shadow:0 2px 4px rgba(0,0,0,.3);font-family:"Open Sans",sans-serif;font-weight:600;font-size:16px;color:#555;display:flex;align-items:center;justify-content:center}
.slides{left:40px;top:231px;display:flex;gap:6px}
.slides span{width:39px;height:18px;background:#2f7d06;transform:skewX(-12deg);color:#fff;font-style:italic;font-weight:700;font-size:12px;display:flex;align-items:center;justify-content:center}
.hero-visual{left:388px;top:12px;width:409px;height:256px;border-radius:8px 8px 0 0;background:linear-gradient(#f4f4f4,#e4eedb);border:10px solid #3a3a3a;border-bottom:0}

/* services */
.services{left:0;top:401px;width:844px;height:163px;display:flex}
.service{position:relative;width:281.3px;height:163px;background:linear-gradient(#fafafa,#ececec);border-right:1px solid #fff}
.service h3{position:absolute;left:36px;top:21px;font-size:13.5px;color:var(--green);font-weight:700;white-space:nowrap}
.service p{position:absolute;left:36px;top:54px;font-size:10.5px;line-height:15px;color:#222;white-space:nowrap}
.service .art{position:absolute;left:218px;top:44px;width:34px;height:62px;border-radius:6px;background:radial-gradient(#fff,#cfcfcf)}
.btn-more{position:absolute;right:16px;top:123px;width:83px;height:26px;background:linear-gradient(var(--green-light),var(--green));transform:skewX(-8deg);color:#fff;font-family:"Open Sans",sans-serif;font-weight:600;font-size:12px;display:flex;align-items:center;justify-content:center}

/* why */
.section-title{font-family:"Open Sans",sans-serif;font-weight:600;font-size:16.5px;color:var(--heading)}
.why-title{left:36px;top:584px}
.feature{width:230px;white-space:normal}
.feature svg{float:left;margin:0 9px 3px 0}
.feature h4{font-weight:400;font-size:13.5px;color:var(--green);margin:0 0 4px;white-space:nowrap}
.feature p{font-size:10.4px;line-height:15px;color:var(--muted)}

/* testimonials */
.sidebar{left:563px;top:564px;width:1px;height:371px;background:#e6e6e6}
.clients-title{left:605px;top:584px}
.quote{left:575px;width:252px;height:83px;background:var(--soft);border-radius:3px;padding:18px 0 0 29px;font-size:10.5px}
.quote em{display:block;line-height:14.6px;color:#111;white-space:nowrap}
.quote .mark{position:absolute;top:5px;font-family:Georgia,serif;font-size:24px;color:#ccc;line-height:1}
.quote .who{position:absolute;left:29px;bottom:9px;color:var(--green-bright);font-size:10.5px}
.quote .read{position:absolute;right:24px;bottom:9px;font-style:italic;font-weight:700;color:#111;font-size:10px}
.more-testimonials{left:604px;top:906px;font-family:"Open Sans",sans-serif;font-weight:700;font-size:12.5px;color:var(--green-dark)}

/* footer */
.site-footer{left:0;top:935px;width:844px;height:77px;background:radial-gradient(ellipse at 40% 0,#6cc41d,#44a00c 70%)}
.footer-nav{left:35px;top:966px;color:#fff;font-size:11px}
.copyright{left:35px;top:1018px;font-size:11px;color:#444}
</style>
</head>
<body>
<div class="page">
  <header class="abs site-header">
    <div class="abs brand">
      <div class="brand-name">BrightLoop</div>
      <div class="brand-tag">Social media marketing</div>
    </div>
    <div class="abs social social-follow">Follow us on Chirpline! <span class="sq" style="background:#6fc3e8"></span></div>
    <div class="abs social social-fan">Become a Fan! <span class="sq" style="background:#3b5a99"></span></div>
  </header>

  <nav class="abs main-nav"><a>Home</a><a>Services</a><a>Order</a><a>Contact</a></nav>

  <section class="abs hero">
    <h1 class="abs hero-title">Establish</h1>
    <p class="abs hero-text">Lorem ipsum dolor sit amet, consectetur adipiscing elit. In vel leo orci, vitae congue ligula. Fusce ac neque et erat aliquet venenatis eleifend a ante. Integer laoreet dignissim ante eget sollicitudin. Maecenas ut metus et ante vulputate posuere a et dolor. Sed vel mauris pulvinar enim vehicula congue.</p>
    <div class="abs btn-try">TRY NOW</div>
    <div class="abs slides"><span>1</span><span>2</span><span>3</span></div>
    <div class="abs hero-visual" role="img" aria-label="Laptop screen showing a rising growth chart on grid paper, with a hand drawing the peak in pencil"></div>
  </section>

  <section class="abs services">
    <article class="service">
      <h3>Establish Social Media Presence</h3>
      <p>Lorem ipsum dolor sit amet,<br>consectetur adipiscing elit. In vel<br>leo orci, vitae congue ligula.<br>Fusce ac neque et erat aliquet<br>venenatis eleifend a ante.</p>
      <div class="art" role="img" aria-label="Light bulb"></div>
      <div class="btn-more">Read more</div>
    </article>
    <article class="service">
      <h3>Management and advertising</h3>
      <p>Lorem ipsum dolor sit amet,<br>consectetur adipiscing elit. In vel<br>leo orci, vitae congue ligula.<br>Fusce ac neque et erat aliquet<br>venenatis eleifend a ante.</p>
      <div class="art" role="img" aria-label="Silver gear"></div>
      <div class="btn-more">Read more</div>
    </article>
    <article class="service">
      <h3>Analyze and Engage</h3>
      <p>Lorem ipsum dolor sit amet,<br>consectetur adipiscing elit. In vel<br>leo orci, vitae congue ligula.<br>Fusce ac neque et erat aliquet<br>venenatis eleifend a ante.</p>
      <div class="art" role="img" aria-label="Flat screen monitor"></div>
      <div class="btn-more">Read more</div>
    </article>
  </section>

  <h2 class="abs section-title why-title">Why use BrightLoop?</h2>

  <div class="abs feature" style="left:36px;top:626px">
    <svg width="40" height="40" viewBox="0 0 40 40"><rect width="40" height="40" fill="#3f8a12"/><polyline points="6,32 14,20 22,25 34,9" fill="none" stroke="#fff" stroke-width="3"/><polyline points="6,24 13,14 21,17 33,7" fill="none" stroke="#fff" stroke-width="1.5" opacity=".6"/></svg>
    <h4>Lorem ipsum dolor sit amet</h4>
    <p>Donec nec semper neque. Nunc vulputate, odio quis vulputate rhoncus, nunc nulla tincidunmauris, nec eleifend nisl orci id ante. Quisque ultricies pulvinar hendrerit. Quisque velit sem, dignissim et lobortis at, fringilla a nisi. Sed tristique volutpat convallis.</p>
  </div>
  <div class="abs feature" style="left:285px;top:626px">
    <svg width="40" height="40" viewBox="0 0 40 40"><rect x="3" y="5" width="32" height="32" rx="5" fill="none" stroke="#3f8a12" stroke-width="4"/><polyline points="10,19 18,28 37,4" fill="none" stroke="#3f8a12" stroke-width="6"/></svg>
    <h4>Lorem ipsum dolor sit amet</h4>
    <p>Donec nec semper neque. Nunc vulputate, odio quis vulputate rhoncus, nunc nulla tincidunmauris, nec eleifend nisl orci id ante. Quisque ultricies pulvinar hendrerit. Quisque velit sem, dignissim et lobortis at, fringilla a nisi. Sed tristique volutpat convallis.</p>
  </div>
  <div class="abs feature" style="left:36px;top:784px">
    <svg width="40" height="40" viewBox="0 0 40 40" fill="#3f8a12"><circle cx="13" cy="7" r="6"/><path d="M2 24a11 9 0 0 1 22 0z"/><circle cx="28" cy="20" r="6"/><path d="M17 38a11 10 0 0 1 22 0z"/></svg>
    <h4>Lorem ipsum dolor sit amet</h4>
    <p>Donec nec semper neque. Nunc vulputate, odio quis vulputate rhoncus, nunc nulla tincidunmauris, nec eleifend nisl orci id ante. Quisque ultricies pulvinar hendrerit. Quisque velit sem, dignissim et lobortis at, fringilla a nisi. Sed tristique volutpat convallis.</p>
  </div>
  <div class="abs feature" style="left:285px;top:784px">
    <svg width="40" height="40" viewBox="0 0 40 40" fill="#3f8a12"><rect x="2" y="5" width="36" height="34" rx="3" fill="none" stroke="#3f8a12" stroke-width="3"/><rect x="2" y="5" width="36" height="7"/><rect x="9" y="1" width="4" height="8"/><rect x="27" y="1" width="4" height="8"/><g><rect x="8" y="16" width="5" height="5"/><rect x="17" y="16" width="5" height="5"/><rect x="26" y="16" width="5" height="5"/><rect x="8" y="24" width="5" height="5"/><rect x="17" y="24" width="5" height="5"/><rect x="26" y="24" width="5" height="5"/><rect x="8" y="31" width="5" height="4"/><rect x="17" y="31" width="5" height="4"/></g></svg>
    <h4>Lorem ipsum dolor sit amet</h4>
    <p>Donec nec semper neque. Nunc vulputate, odio quis vulputate rhoncus, nunc nulla tincidunmauris, nec eleifend nisl orci id ante. Quisque ultricies pulvinar hendrerit. Quisque velit sem, dignissim et lobortis at, fringilla a nisi. Sed tristique volutpat convallis.</p>
  </div>

  <aside class="abs sidebar"></aside>
  <h2 class="abs section-title clients-title">Words from clients</h2>
  <blockquote class="abs quote" style="top:611px"><span class="mark" style="left:8px">&ldquo;</span><span class="mark" style="right:8px">&rdquo;</span><em>Lorem ipsum dolor sit amet, consectetur<br>adipiscing elit. In id odio enim, nec feugiat<br>nulla. Donec nec .</em><span class="who">Happy Client Name</span><span class="read">read more</span></blockquote>
  <blockquote class="abs quote" style="top:713px"><span class="mark" style="left:8px">&ldquo;</span><span class="mark" style="right:8px">&rdquo;</span><em>Lorem ipsum dolor sit amet, consectetur<br>adipiscing elit. In id odio enim, nec feugiat<br>nulla. Donec nec .</em><span class="who">Happy Client Name</span><span class="read">read more</span></blockquote>
  <blockquote class="abs quote" style="top:813px"><span class="mark" style="left:8px">&ldquo;</span><span class="mark" style="right:8px">&rdquo;</span><em>Lorem ipsum dolor sit amet, consectetur<br>adipiscing elit. In id odio enim, nec feugiat<br>nulla. Donec nec .</em><span class="who">Happy Client Name</span><span class="read">read more</span></blockquote>
  <a class="abs more-testimonials">See more testimonials</a>

  <footer class="abs site-footer"></footer>
  <nav class="abs footer-nav">Home | Services | Order | Contact</nav>
  <p class="abs copyright">&copy; 2011 BrightLoop.com</p>
</div>
</body>
</html>
```